Zielgruppe
Wir betreiben unter https://www.belvanto.de/ eine B2B-Software zur Automatisierung der Abrechnungsprozesse (Subscription Management) Zielgruppe = 100 % B2B
Aufgabenstellung
Wir planen, die Vorlage in erste Linie für ein Direktmailing zu nutzen. Das Briefpapier soll aber genauso für normale Kundenanschreiben (Mahnung etc.) passen. Wir nutzen selbst Libre Office, das Ergebnis sollte sich also dort so einfach wie möglich integrieren lassen.

```html
<!DOCTYPE html>
<html lang="de">
<head>
<meta charset="utf-8">
<title>Belvanto Briefbogen</title>
<link href="https://fonts.googleapis.com/css2?family=Arimo:wght@400&family=Open+Sans:wght@400;700&display=swap" rel="stylesheet">
<style>
:root{
  --stage:#3a3d42;
  --paper:#ffffff;
  --brand-blue:#259ad8;
  --brand-green:#92c02a;
  --ink:#1d1d1f;
  --muted:#333a40;
  --rule:#9aa0a6;
  --sign:#1c2f8a;
}
*{margin:0;padding:0;box-sizing:border-box}
html,body{width:1200px;height:945px;overflow:hidden;background:var(--stage)}
.sheet{position:absolute;left:280px;top:20px;width:640px;height:905px;background:var(--paper);overflow:hidden;border-top:4px solid var(--brand-blue);font-family:"Open Sans",sans-serif;color:var(--ink)}
.brand{position:absolute;left:330px;top:52px;display:flex;align-items:center;gap:10px}
.brand-name{font-family:"Open Sans",sans-serif;font-weight:700;font-size:38px;color:var(--brand-blue);letter-spacing:.5px}
.brand-mark{width:30px;height:30px;border-radius:50%;background:var(--brand-green)}
.sender-line{position:absolute;left:70px;top:128px;font-size:6.5px;color:var(--muted);border-bottom:.6px solid var(--muted);padding-bottom:1px}
.sender-line .sep{color:var(--brand-blue);padding:0 3px}
.contact{position:absolute;left:470px;top:120px;padding-left:10px;border-left:1px solid var(--muted);font-size:8.5px;line-height:12px;color:var(--muted)}
.contact .gap{height:6px}
.contact .row{display:flex;align-items:center;gap:5px}
.contact svg{width:8px;height:8px;fill:var(--brand-blue)}
.fold{position:absolute;left:0;width:14px;border-top:.7px solid var(--rule)}
.letter{position:absolute;left:72px;top:205px;width:480px;font-family:"Arimo",sans-serif;font-size:11px;line-height:14px;color:var(--ink)}
.letter p{margin-bottom:12px}
.letter .subject{margin-bottom:12px}
.signature{width:120px;height:40px;background:linear-gradient(90deg,#dfe3f2,#eef0f8);margin:4px 0 6px}
.signer{margin-top:0}
.footer-art{position:absolute;left:0;bottom:0;width:640px;height:170px}
.footer-info{position:absolute;left:60px;top:770px;display:flex;gap:18px;font-size:7.5px;line-height:11px;color:var(--muted)}
.footer-info .col{padding-right:18px;border-right:1px solid var(--muted)}
.footer-info .col:last-child{border-right:none}
.web{position:absolute;right:40px;bottom:14px;font-size:12px;color:#fff;letter-spacing:.3px}
</style>
</head>
<body>
<main class="sheet">
  <div class="brand">
    <span class="brand-name">Belvanto</span>
    <span class="brand-mark"></span>
  </div>

  <div class="sender-line">Karosto IT Services GmbH<span class="sep">|</span>Lindenweg 4<span class="sep">|</span>83022 Rosenheim</div>

  <address class="contact">
    <div>Karosto IT Services GmbH</div>
    <div>Lindenweg 4</div>
    <div>83022 Rosenheim</div>
    <div class="gap"></div>
    <div class="row"><svg viewBox="0 0 10 10"><path d="M2 0.5l2 2-1 1.2c.6 1.3 1.6 2.3 2.9 2.9L7.1 5.6l2 2-1.4 1.8C4.2 9 1 5.8.6 2z"/></svg>(0 80 31) 47 20 1500</div>
    <div class="row"><svg viewBox="0 0 10 10"><rect x="1" y="3" width="8" height="6"/><rect x="2.5" y="0.5" width="5" height="2"/></svg>(0 80 31) 61 358 - 40</div>
    <div class="row"><svg viewBox="0 0 10 10"><path d="M0 2h10v6H0z M0 2l5 3.5L10 2" /></svg>info@belvanto.de</div>
  </address>

  <span class="fold" style="top:300px"></span>
  <span class="fold" style="top:428px"></span>
  <span class="fold" style="top:600px"></span>

  <article class="letter">
    <p class="subject">Betreffzeile</p>
    <p>Sehr geehrte Damen und Herren,</p>
    <p>In sollicitudin, metus et posuere blandit, erat dui bibendum eros, id vestibulum sem justo vel mauris. Ut tempor dolor ut justo vulputate, eu blandit libero faucibus. In laoreet, massa non ultricies tempor, est enim auctor mi, sit amet venenatis massa augue in justo. Praesent eu tincidunt diam. Maecenas id mi efficitur tellus interdum consectetur vel sed ante. Sed suscipit quis.</p>
    <p>Sed nunc est, iaculis vel enim ut, fringilla commodo lorem. Pellentesque facilisis tempus lorem eget porttitor. Morbi accumsan, nulla accumsan mollis maximus, lectus diam venenatis odio, quis bibendum elit ex a arcu. Fusce turpis erat, euismod sit amet dolor eu, hendrerit rhoncus libero. Phasellus convallis, mi vel pharetra sollicitudin, nisi purus maximus est, nec lobortis dolor enim et.</p>
    <p style="margin-bottom:0">Mit freundlichen Grüßen</p>
    <div class="signature" role="img" aria-label="Handschriftliche Unterschrift"></div>
    <p class="signer">Jonas Beispiel, LL.M.</p>
  </article>

  <svg class="footer-art" viewBox="0 0 640 170" preserveAspectRatio="none" aria-hidden="true">
    <path d="M0 90 C120 120 260 150 400 170 L0 170 Z" fill="var(--brand-green)"/>
    <path d="M0 104 C130 132 260 158 360 170 L0 170 Z" fill="#fff"/>
    <path d="M0 110 C150 150 330 175 450 155 C520 142 580 132 640 128 L640 170 L0 170 Z" fill="var(--brand-blue)"/>
  </svg>

  <div class="footer-info">
    <div class="col">Bankverbindung:<br>Musterbank Nordtal</div>
    <div class="col">Steuernummer: 204/318/00000<br>Umsatzsteuer-ID-Nr.: DE 417293000</div>
    <div class="col">BIC: MUSTDE55XXX<br>IBAN: DE12 5500 0000 0123 45678 90</div>
  </div>

  <div class="web">www.belvanto.de</div>
</main>
</body>
</html>
```